Webdesign für KFZ-Service-Betrieb
Zielgruppe
Wartung, Reparatur und Instandsetzung von Kraftfahrzeugen aller Marken.
Reifenhandel, Old- und Youngtimer-Service, An- und Verkauf von Fahrzeugen.
Aufgabenstellung
Firmenfarbe ist blau.
Moderner, Übersichtlicher und Transparenter Auftritt erwünscht.

```html
<!DOCTYPE html>
<html lang="de">
<head>
<meta charset="utf-8">
<title>Autohaus Brenner – Autoservice nach Maß</title>
<link href="https://fonts.googleapis.com/css2?family=Roboto:ital,wght@0,300;0,400;0,500;0,700;1,300&family=Roboto+Slab:wght@400&display=swap" rel="stylesheet">
<style>
:root{
  --brand:#0d2f9c;
  --brand-dark:#0a2a8a;
  --text:#333;
  --muted:#777;
  --page:#f4f4f4;
  --strip:#ebebeb;
  --panel:#cfd6e6;
  --white:#fff;
  --line:#b7c0d6;
}
*{box-sizing:border-box;margin:0;padding:0}
html,body{width:947px;height:1200px;overflow:hidden}
body{font-family:'Roboto',sans-serif;background:var(--page);color:var(--text);position:relative}
.wrap{width:563px;margin:0 auto;position:relative}

/* header */
.site-header{height:49px;background:var(--white)}
.site-header .wrap{display:flex;justify-content:space-between;align-items:center;height:49px}
.brand{display:flex;align-items:center;gap:6px;color:var(--brand);font-family:'Roboto',sans-serif}
.brand-mark{width:10px;height:10px;border-radius:50%;background:var(--brand)}
.brand-name{font-size:14px;font-weight:400;letter-spacing:.2px}
.brand-tag{font-size:6.5px;color:var(--brand);display:block;text-align:right;margin-top:1px}
.contact{display:flex;gap:10px;align-items:center;font-size:8px;color:var(--muted);font-weight:300}
.contact-item{display:flex;align-items:center;gap:8px;text-align:right;line-height:10px}
.contact-sep{width:1px;height:24px;background:#ddd}

/* hero */
.hero{position:relative;height:246px;background:linear-gradient(135deg,#5c6f86 0%,#8a96a4 35%,#3e4650 70%,#6f7478 100%)}
.main-nav{position:absolute;top:0;left:0;right:0;height:25px;border-bottom:1px solid rgba(255,255,255,.5)}
.main-nav ul{list-style:none;display:flex;justify-content:space-between;width:547px;margin:0 auto;padding-left:20px;height:25px;align-items:center}
.main-nav a{font-size:8.3px;color:var(--white);text-decoration:none;font-weight:400}
.main-nav a.active{color:#3a5bd0}
.hero-panel{position:absolute;left:0;top:90px;width:607px;height:93px;background:rgba(255,255,255,.88)}
.hero-panel .inner{margin-left:192px;padding-top:9px}
.hero-title{font-size:20px;font-weight:700;color:var(--brand);letter-spacing:-.2px}
.hero-text{font-size:7.4px;color:#666;font-weight:500;line-height:9.5px;margin-top:4px;text-transform:uppercase}
.hero-text strong{color:var(--brand)}
.btn{display:inline-block;margin-top:6px;background:var(--brand);color:var(--white);font-size:8.5px;font-weight:500;width:99px;height:22px;line-height:22px;text-align:center;text-decoration:none}
.hero-dots{position:absolute;right:196px;bottom:8px;display:flex;gap:4px}
.hero-dots span{width:7px;height:7px;border:1px solid var(--white);border-radius:50%}
.hero-dots span.on{border-color:var(--white);background:#2a55d4}

/* brands */
.brand-strip{height:52px;background:var(--strip)}
.brand-strip .wrap{display:flex;align-items:center;justify-content:space-between;height:52px;width:580px}
.badges{display:flex;gap:16px;align-items:center}
.badge{width:22px;height:22px;border-radius:50%;background:#c4c8d0}
.badge.sq{border-radius:3px;width:20px;height:18px}

/* section titles */
.section-title{text-align:center;font-size:16px;font-weight:400;color:#333;letter-spacing:.3px}

/* services */
.services{padding-top:26px}
.tiles{display:grid;grid-template-columns:repeat(3,178px);gap:15px;margin-top:9px}
.tile{position:relative;height:98px;overflow:hidden}
.tile-img{position:absolute;inset:0}
.tile-bar{position:absolute;left:0;right:0;bottom:0;height:27px;background:rgba(60,60,60,.75);display:flex;align-items:center;justify-content:space-between;padding:0 7px 0 8px;color:var(--white);font-size:11px;font-weight:300}
.arrow-circle{width:12px;height:12px}
.tile.care{background:var(--white)}
.care-name{position:absolute;left:0;right:0;top:18px;text-align:center;color:#d42a25;font-weight:700;font-size:13px;line-height:15px}
.tile.care .tile-bar{background:#7a7a7a}

/* team */
.team{padding-top:30px}
.cards{display:grid;grid-template-columns:repeat(4,129px);gap:16px;margin-top:9px}
.card{background:var(--white);height:217px;padding:7px 7px 0;box-shadow:0 0 2px rgba(0,0,0,.15)}
.card-photo{height:133px}
.card-name{font-size:9.5px;color:var(--brand);margin-top:6px;padding-left:1px}
.card-role{font-size:6.8px;color:#444;line-height:8.3px;margin-top:4px;height:17px;padding-left:1px}
.card-phone{display:flex;align-items:center;gap:5px;font-size:8px;color:var(--muted);font-weight:300;margin-top:5px;padding-left:1px}
.card-phone + .card-phone{margin-top:5px}
.pager{display:flex;justify-content:center;gap:3px;margin-top:9px}
.pager span{width:5px;height:5px;border-radius:50%;background:#a9b4d2}
.pager span.on{background:var(--brand)}

/* info panels */
.info{display:grid;grid-template-columns:274px 274px;gap:15px;margin-top:22px}
.panel{background:var(--panel);height:207px;padding:8px 7px 0}
.panel h2{font-size:11px;font-weight:500;color:var(--brand);padding-left:1px}
.quote{display:flex;gap:10px;padding:8px 0 7px 1px;border-bottom:1px dashed var(--line)}
.quote-avatar{flex:none;width:39px;height:39px;border-radius:50%;border:2px solid var(--white)}
.quote p{font-size:7.4px;font-style:italic;font-weight:300;color:#555;line-height:9.4px;margin-left:0}
.quote cite{display:block;font-style:normal;font-size:7.8px;color:#333;margin-top:0}
.panel .pager{margin-top:8px}
.offers{list-style:none;margin-top:4px}
.offers li{font-size:7.8px;color:#333;line-height:9.5px;padding:7px 1px 6px;border-bottom:1px dashed var(--line)}
.offers li:last-child{border-bottom:none}

/* footer */
.site-footer{position:absolute;left:0;right:0;top:1158px}
.footer-links{height:25px;background:var(--strip)}
.footer-links ul{list-style:none;display:flex;gap:19px;height:25px;align-items:center;padding-left:8px}
.footer-links a{font-size:8px;color:#888;text-decoration:none}
.footer-links a.active{color:var(--brand)}
.copyright{text-align:center;font-size:6.5px;color:#999;margin-top:4px}
</style>
</head>
<body>

<header class="site-header">
  <div class="wrap">
    <div class="brand">
      <span class="brand-mark"></span>
      <div>
        <span class="brand-name">Autohaus Brenner</span>
        <span class="brand-tag">Autoservice nach Maß</span>
      </div>
    </div>
    <div class="contact">
      <div class="contact-item">
        <svg width="14" height="14" viewBox="0 0 24 24" fill="#0d2f9c"><path d="M6.6 10.8c1.4 2.8 3.8 5.1 6.6 6.6l2.2-2.2c.3-.3.7-.4 1-.2 1.1.4 2.3.6 3.6.6.6 0 1 .4 1 1V20c0 .6-.4 1-1 1C10.6 21 3 13.4 3 4c0-.6.4-1 1-1h3.5c.6 0 1 .4 1 1 0 1.3.2 2.5.6 3.6.1.3 0 .7-.2 1L6.6 10.8z"/></svg>
        <div>info@autohaus-brenner.de<br>04321 / 55 60</div>
      </div>
      <span class="contact-sep"></span>
      <div class="contact-item">
        <svg width="18" height="18" viewBox="0 0 24 24" fill="none" stroke="#0d2f9c" stroke-width="2"><circle cx="12" cy="12" r="10"/><path d="M12 6v6l4 3"/></svg>
        <div>Mo-Fr: 07:30 - 18:00<br>Sa: 09:00 -12:00</div>
      </div>
    </div>
  </div>
</header>

<section class="hero" role="img" aria-label="Werkstattfoto mit gestapelten Reifen im Vordergrund">
  <nav class="main-nav">
    <ul>
      <li><a class="active" href="#">STARTSEITE</a></li>
      <li><a href="#">LEISTUNGEN</a></li>
      <li><a href="#">PHILOSOPHIE</a></li>
      <li><a href="#">FIRMENGESCHICHTE</a></li>
      <li><a href="#">ZUFRIEDENE KUNDEN</a></li>
      <li><a href="#">TEAM UND KONTAKT</a></li>
    </ul>
  </nav>
  <div class="hero-panel">
    <div class="inner">
      <h1 class="hero-title">SOMMERRÄDER KAUFEN!</h1>
      <p class="hero-text">Bei uns gibt es Markenreifen schon ab <strong>39 €</strong> Wir liefern alle Fabrikate zu günstigen Preisen.<br>Fragen Sie nach Ihren individuellen Angebot.</p>
      <a class="btn" href="#">CONTACT US</a>
    </div>
  </div>
  <div class="hero-dots"><span class="on"></span><span></span><span></span><span></span></div>
</section>

<section class="brand-strip">
  <div class="wrap">
    <svg width="10" height="24" viewBox="0 0 10 24" fill="none" stroke="#666" stroke-width="1"><path d="M9 1L1 12l8 11"/></svg>
    <div class="badges">
      <span class="badge"></span><span class="badge"></span><span class="badge"></span><span class="badge"></span>
      <span class="badge sq"></span><span class="badge sq"></span><span class="badge sq"></span><span class="badge"></span>
      <span class="badge sq"></span><span class="badge"></span><span class="badge"></span><span class="badge sq"></span>
      <span class="badge"></span><span class="badge"></span>
    </div>
    <svg width="10" height="24" viewBox="0 0 10 24" fill="none" stroke="#666" stroke-width="1"><path d="M1 1l8 11-8 11"/></svg>
  </div>
</section>

<main class="wrap">
  <section class="services">
    <h2 class="section-title">LEISTUNGEN</h2>
    <div class="tiles">
      <div class="tile">
        <div class="tile-img" role="img" aria-label="Mechaniker arbeitet unter einem Fahrzeug" style="background:linear-gradient(135deg,#8c7a6a,#3a3f52 60%,#b9b0a8)"></div>
        <div class="tile-bar">SERVICE <svg class="arrow-circle" viewBox="0 0 12 12" fill="none" stroke="#fff" stroke-width=".8"><circle cx="6" cy="6" r="5.5"/><path d="M5 3.5L7.5 6 5 8.5"/></svg></div>
      </div>
      <div class="tile">
        <div class="tile-img" role="img" aria-label="Werkstatthalle mit Hebebühnen" style="background:linear-gradient(180deg,#c8ccd2,#8b919a 60%,#5d6066)"></div>
        <div class="tile-bar">UNFALLINSTANDSETZUNG <svg class="arrow-circle" viewBox="0 0 12 12" fill="none" stroke="#fff" stroke-width=".8"><circle cx="6" cy="6" r="5.5"/><path d="M5 3.5L7.5 6 5 8.5"/></svg></div>
      </div>
      <div class="tile">
        <div class="tile-img" role="img" aria-label="Verkaufsgespräch am Schreibtisch" style="background:linear-gradient(90deg,#6b4a33,#c9a47a 55%,#e7d6bc)"></div>
        <div class="tile-bar">VERKAUF <svg class="arrow-circle" viewBox="0 0 12 12" fill="none" stroke="#fff" stroke-width=".8"><circle cx="6" cy="6" r="5.5"/><path d="M5 3.5L7.5 6 5 8.5"/></svg></div>
      </div>
      <div class="tile">
        <div class="tile-img" role="img" aria-label="Fahrzeug in der Waschanlage" style="background:linear-gradient(90deg,#2c4a8a,#b9bcc2 50%,#2c4a8a)"></div>
        <div class="tile-bar">FAHRZEUGPFLEGE <svg class="arrow-circle" viewBox="0 0 12 12" fill="none" stroke="#fff" stroke-width=".8"><circle cx="6" cy="6" r="5.5"/><path d="M5 3.5L7.5 6 5 8.5"/></svg></div>
      </div>
      <div class="tile">
        <div class="tile-img" role="img" aria-label="Mechaniker montiert ein Rad" style="background:linear-gradient(135deg,#2b3558,#b0242a 55%,#3a3a3a)"></div>
        <div class="tile-bar">KLEINE PREISLISTE <svg class="arrow-circle" viewBox="0 0 12 12" fill="none" stroke="#fff" stroke-width=".8"><circle cx="6" cy="6" r="5.5"/><path d="M5 3.5L7.5 6 5 8.5"/></svg></div>
      </div>
      <div class="tile care">
        <div class="care-name">GLANZPRO<br>Pflegestation</div>
        <div class="tile-bar">GLANZPRO - SERVICE <svg class="arrow-circle" viewBox="0 0 12 12" fill="none" stroke="#fff" stroke-width=".8"><circle cx="6" cy="6" r="5.5"/><path d="M5 3.5L7.5 6 5 8.5"/></svg></div>
      </div>
    </div>
  </section>

  <section class="team">
    <h2 class="section-title">OUR TEAM</h2>
    <div class="cards">
      <article class="card">
        <div class="card-photo" role="img" aria-label="Porträtfoto Markus Helbig" style="background:linear-gradient(180deg,#c9743a,#a8a19a 60%,#3a3a3e)"></div>
        <h3 class="card-name">Markus Helbig</h3>
        <p class="card-role">Geschäftsführer ,Betriebswirt,<br>Kfz-Meister</p>
        <p class="card-phone"><svg width="7" height="7" viewBox="0 0 24 24" fill="#0d2f9c"><path d="M6.6 10.8c1.4 2.8 3.8 5.1 6.6 6.6l2.2-2.2c.3-.3.7-.4 1-.2 1.1.4 2.3.6 3.6.6.6 0 1 .4 1 1V20c0 .6-.4 1-1 1C10.6 21 3 13.4 3 4c0-.6.4-1 1-1h3.5c.6 0 1 .4 1 1 0 1.3.2 2.5.6 3.6.1.3 0 .7-.2 1z"/></svg>04321/556200</p>
        <p class="card-phone"><svg width="7" height="7" viewBox="0 0 24 24" fill="#0d2f9c"><path d="M6.6 10.8c1.4 2.8 3.8 5.1 6.6 6.6l2.2-2.2c.3-.3.7-.4 1-.2 1.1.4 2.3.6 3.6.6.6 0 1 .4 1 1V20c0 .6-.4 1-1 1C10.6 21 3 13.4 3 4c0-.6.4-1 1-1h3.5c.6 0 1 .4 1 1 0 1.3.2 2.5.6 3.6.1.3 0 .7-.2 1z"/></svg>04321/556222</p>
      </article>
      <article class="card">
        <div class="card-photo" role="img" aria-label="Porträtfoto Ingrid Helbig" style="background:linear-gradient(180deg,#6b5a4a,#b58a6c 55%,#4d7a4a)"></div>
        <h3 class="card-name">Ingrid Helbig</h3>
        <p class="card-role">Verwaltung und Kaufmännischer<br>Betrieb</p>
        <p class="card-phone"><svg width="7" height="7" viewBox="0 0 24 24" fill="#0d2f9c"><path d="M6.6 10.8c1.4 2.8 3.8 5.1 6.6 6.6l2.2-2.2c.3-.3.7-.4 1-.2 1.1.4 2.3.6 3.6.6.6 0 1 .4 1 1V20c0 .6-.4 1-1 1C10.6 21 3 13.4 3 4c0-.6.4-1 1-1h3.5c.6 0 1 .4 1 1 0 1.3.2 2.5.6 3.6.1.3 0 .7-.2 1z"/></svg>04321/5560</p>
        <p class="card-phone"><svg width="7" height="7" viewBox="0 0 24 24" fill="#0d2f9c"><path d="M6.6 10.8c1.4 2.8 3.8 5.1 6.6 6.6l2.2-2.2c.3-.3.7-.4 1-.2 1.1.4 2.3.6 3.6.6.6 0 1 .4 1 1V20c0 .6-.4 1-1 1C10.6 21 3 13.4 3 4c0-.6.4-1 1-1h3.5c.6 0 1 .4 1 1 0 1.3.2 2.5.6 3.6.1.3 0 .7-.2 1z"/></svg>04321/556222</p>
      </article>
      <article class="card">
        <div class="card-photo" role="img" aria-label="Porträtfoto Sabine Kranzl" style="background:linear-gradient(180deg,#9a8f86,#c9aa94 55%,#2f7a4e)"></div>
        <h3 class="card-name">Sabine Kranzl</h3>
        <p class="card-role">Controlling Rechnungswesen und<br>Finanzbuchhaltung</p>
        <p class="card-phone"><svg width="7" height="7" viewBox="0 0 24 24" fill="#0d2f9c"><path d="M6.6 10.8c1.4 2.8 3.8 5.1 6.6 6.6l2.2-2.2c.3-.3.7-.4 1-.2 1.1.4 2.3.6 3.6.6.6 0 1 .4 1 1V20c0 .6-.4 1-1 1C10.6 21 3 13.4 3 4c0-.6.4-1 1-1h3.5c.6 0 1 .4 1 1 0 1.3.2 2.5.6 3.6.1.3 0 .7-.2 1z"/></svg>04321/556100</p>
        <p class="card-phone"><svg width="7" height="7" viewBox="0 0 24 24" fill="#0d2f9c"><path d="M6.6 10.8c1.4 2.8 3.8 5.1 6.6 6.6l2.2-2.2c.3-.3.7-.4 1-.2 1.1.4 2.3.6 3.6.6.6 0 1 .4 1 1V20c0 .6-.4 1-1 1C10.6 21 3 13.4 3 4c0-.6.4-1 1-1h3.5c.6 0 1 .4 1 1 0 1.3.2 2.5.6 3.6.1.3 0 .7-.2 1z"/></svg>04321/556222</p>
      </article>
      <article class="card">
        <div class="card-photo" role="img" aria-label="Porträtfoto Jonas Pfeiffer" style="background:linear-gradient(180deg,#d5d2cc,#b99682 55%,#2d4fa6)"></div>
        <h3 class="card-name">Jonas Pfeiffer</h3>
        <p class="card-role">Mechatroniker und Spezialist für<br>Elektronik im Fahrzeug</p>
        <p class="card-phone"><svg width="7" height="7" viewBox="0 0 24 24" fill="#0d2f9c"><path d="M6.6 10.8c1.4 2.8 3.8 5.1 6.6 6.6l2.2-2.2c.3-.3.7-.4 1-.2 1.1.4 2.3.6 3.6.6.6 0 1 .4 1 1V20c0 .6-.4 1-1 1C10.6 21 3 13.4 3 4c0-.6.4-1 1-1h3.5c.6 0 1 .4 1 1 0 1.3.2 2.5.6 3.6.1.3 0 .7-.2 1z"/></svg>04321/5560</p>
        <p class="card-phone"><svg width="7" height="7" viewBox="0 0 24 24" fill="#0d2f9c"><path d="M6.6 10.8c1.4 2.8 3.8 5.1 6.6 6.6l2.2-2.2c.3-.3.7-.4 1-.2 1.1.4 2.3.6 3.6.6.6 0 1 .4 1 1V20c0 .6-.4 1-1 1C10.6 21 3 13.4 3 4c0-.6.4-1 1-1h3.5c.6 0 1 .4 1 1 0 1.3.2 2.5.6 3.6.1.3 0 .7-.2 1z"/></svg>04321/556222</p>
      </article>
    </div>
    <div class="pager"><span class="on"></span><span></span></div>
  </section>

  <section class="info">
    <div class="panel">
      <h2>ZUFRIEDENE KUNDEN</h2>
      <blockquote class="quote">
        <div class="quote-avatar" role="img" aria-label="Kundenfoto R. Lenz" style="background:linear-gradient(180deg,#c9b6a6,#3d4150)"></div>
        <p>"Habe bei "Brenner" ein Auto für meine Frau gekauft und möchte mich auf diesem Weg nochmals für den hervorragenden Service und die zuvorkommende Art des Herrn Helbig bedanken.Ich kann dieses Autohaus nur weiterempfehlen. Nur selten findet man in der Autobranche noch solche aufrichtigen Geschäftspartner."<cite>R. Lenz</cite></p>
      </blockquote>
      <blockquote class="quote">
        <div class="quote-avatar" role="img" aria-label="Kundenfoto K.T." style="background:linear-gradient(180deg,#d2b7a0,#4a4a55)"></div>
        <p>"Ich möchte mich hiermit Ihren Bewertungen positiv anschließen. Bei Ihnen wird Kundenfreundlichkeit noch großgeschrieben. Ihr Preis-Leistungs-Verhältnis ist nahezu unschlagbar. Ich denke ich habe in Sachen Reifen und Service einen neuen Favoriten gefunden. "<cite>K.T.</cite></p>
      </blockquote>
      <div class="pager"><span class="on"></span><span></span><span></span><span></span></div>
    </div>
    <div class="panel">
      <h2>AKTUELLE ANGEBOTE</h2>
      <ul class="offers">
        <li>10-Punkte</li>
        <li>Frühjahrs-Check nur 19,90 €</li>
        <li>Rädereinlagerung nur 19,90 €</li>
        <li>Räderwäsche nur 16,00€</li>
        <li>Komplettversiegelung des Unterbodens mit GLANZPRO zum kalkulierten Festpreis ab 249,00 €</li>
        <li>Fahrzeugkomplett-aufbereitung inkl. Lackreinigung, Politur &amp; Lackversiegelung, Innenreinigung ab 149,00 €</li>
        <li>Markenreifen ab 39,00 €</li>
      </ul>
    </div>
  </section>
</main>

<footer class="site-footer">
  <div class="footer-links">
    <ul class="wrap">
      <li><a class="active" href="#">Impressum</a></li>
      <li><a href="#">Disclaimer</a></li>
      <li><a href="#">E-Mail</a></li>
      <li><a href="#">Sitemap</a></li>
      <li><a href="#">Login</a></li>
    </ul>
  </div>
  <p class="copyright">© Copyright 2016 Autohaus Brenner GmbH</p>
</footer>

</body>
</html>
```